Business Card for Brevel Coatings

We need a simple, yet out standing business card for our painting company.

Target Market(s)

wealthy; high-end neighborhoods, and businesses

Industry/Entity Type

Painting

Contact Information for Business Card

Name:
Doran Vask

Email:
d.vask@brevel-coatings.com

Website:
Brevel-coatings.com

Phone Number:
(555) 416-9073

Font styles to use
Serif
Sans Serif

Requirements
Must have
• slogan "Fresh Walls Made Easy"
Should not have
• A title attached to the name on the card

```html
<!DOCTYPE html>
<html lang="en">
<head>
<meta charset="utf-8">
<title>Brevel Coatings — Business Card</title>
<link href="https://fonts.googleapis.com/css2?family=Cinzel:wght@400;600;700&family=Crimson+Text:wght@400;600&display=swap" rel="stylesheet">
<style>
  :root {
    --backdrop: #2f3e47;
    --forest: #3e5126;
    --forest-card: #44582a;
    --forest-raised: #566d31;
    --lime: #b4cc3a;
    --lime-text: #8fab2c;
    --paper: #ffffff;
    --ink: #3a4a22;
  }
  * { margin: 0; padding: 0; box-sizing: border-box; }
  html, body {
    width: 1200px; height: 900px; overflow: hidden;
    background: radial-gradient(ellipse at 50% 40%, #3a4b55 0%, var(--backdrop) 75%);
  }
  .canvas { position: relative; width: 1200px; height: 900px; }

  .card {
    position: absolute; left: 300px; width: 600px; height: 343px;
    box-shadow: 0 10px 28px rgba(0,0,0,.35);
    overflow: hidden;
  }
  .card--back { top: 62px; background: var(--forest-card); }
  .card--front { top: 470px; background: var(--paper); }

  .brand {
    position: absolute; text-align: center;
    font-family: "Cinzel", serif;
  }
  .brand__name {
    font-weight: 600; font-size: 44px; letter-spacing: 1px; line-height: 1;
    white-space: nowrap;
  }
  .brand__sub {
    font-weight: 400; font-size: 22px; letter-spacing: 7px; line-height: 1;
    margin-top: 4px; white-space: nowrap;
  }
  .brand__slogan {
    margin-top: 12px; font-size: 13px; letter-spacing: 4px; white-space: nowrap;
  }

  .card--back .brand { left: 0; right: 0; top: 92px; }
  .card--back .brand__name,
  .card--back .brand__sub,
  .card--back .brand__slogan {
    color: var(--forest-raised);
    text-shadow: 0 1px 0 rgba(255,255,255,.06), 0 -1px 0 rgba(0,0,0,.18);
  }

  .card__swoosh { position: absolute; inset: 0; width: 100%; height: 100%; }

  .card--front .brand { left: 110px; width: 400px; top: 22px; }
  .card--front .brand__name { color: var(--forest); }
  .card--front .brand__sub { color: var(--lime-text); }
  .card--front .brand__slogan { color: var(--lime-text); }

  .contact {
    position: absolute; left: 392px; top: 168px; width: 200px;
    font-family: "Crimson Text", serif; color: var(--ink);
  }
  .contact__name {
    font-family: "Cinzel", serif; font-weight: 700; font-size: 22px;
    color: var(--forest); padding-bottom: 3px;
    border-bottom: 1px solid var(--forest); width: 150px;
    white-space: nowrap;
  }
  .contact__list { list-style: none; margin-top: 10px; }
  .contact__item {
    display: flex; align-items: center; gap: 10px;
    font-size: 15px; height: 31px; white-space: nowrap;
  }
  .contact__icon { width: 18px; height: 18px; flex: none; }
</style>
</head>
<body>
<main class="canvas">

  <section class="card card--back" aria-label="Card back">
    <div class="brand">
      <div class="brand__name">BREVEL</div>
      <div class="brand__sub">COATINGS</div>
      <div class="brand__slogan">FRESH WALLS MADE EASY</div>
    </div>
  </section>

  <section class="card card--front" aria-label="Card front">
    <svg class="card__swoosh" viewBox="0 0 600 343" preserveAspectRatio="none" aria-hidden="true">
      <path d="M0,0 L84,0 C24,125 130,298 336,343 L0,343 Z" fill="var(--lime)"/>
      <path d="M0,0 L64,0 C8,125 110,300 300,343 L0,343 Z" fill="var(--forest)"/>
    </svg>

    <div class="brand">
      <div class="brand__name">BREVEL</div>
      <div class="brand__sub">COATINGS</div>
      <div class="brand__slogan">FRESH WALLS MADE EASY</div>
    </div>

    <div class="contact">
      <div class="contact__name">DORAN VASK</div>
      <ul class="contact__list">
        <li class="contact__item">
          <svg class="contact__icon" viewBox="0 0 24 24" aria-hidden="true">
            <path fill="var(--forest)" d="M6.6 10.8a15.1 15.1 0 0 0 6.6 6.6l2.2-2.2a1 1 0 0 1 1-.25 11.4 11.4 0 0 0 3.6.57 1 1 0 0 1 1 1V20a1 1 0 0 1-1 1A17 17 0 0 1 3 4a1 1 0 0 1 1-1h3.5a1 1 0 0 1 1 1c0 1.25.2 2.45.57 3.57a1 1 0 0 1-.25 1z"/>
          </svg>
          <span>(555) 416-9073</span>
        </li>
        <li class="contact__item">
          <svg class="contact__icon" viewBox="0 0 24 24" aria-hidden="true">
            <rect x="2" y="5" width="20" height="14" fill="none" stroke="var(--forest)" stroke-width="1.8"/>
            <path d="M2 5l10 8 10-8M2 19l7-7M22 19l-7-7" fill="none" stroke="var(--forest)" stroke-width="1.6"/>
          </svg>
          <span>d.vask@brevel-coatings.com</span>
        </li>
        <li class="contact__item">
          <svg class="contact__icon" viewBox="0 0 24 24" aria-hidden="true">
            <g fill="none" stroke="var(--forest)" stroke-width="1.5">
              <circle cx="12" cy="12" r="10"/>
              <ellipse cx="12" cy="12" rx="4.5" ry="10"/>
              <path d="M2 12h20M4 7h16M4 17h16"/>
            </g>
          </svg>
          <span>www.brevel-coatings.com</span>
        </li>
      </ul>
    </div>
  </section>

</main>
</body>
</html>
```